Business Card and Letterhead for new company Vardel GreenWorks, Inc.

Vardel GreenWorks, Inc., an engineering and construction firm that provides services for solid waste landfill gas systems, needs a business card and letterhead. We recently had a logo designed but we are open to some tweaks to logo design and color scheme. Generally, we like "earthy" color tones - greens, browns, oranges. This is a sister company - www.talvoriengineering.example.

Target Market(s)

Solid waste landfill companies - Brindle Disposal, Halcott Hauling, etc.

Industry/Entity Type

Engineering and Construction

Contact Information for Business Card

Name, Title, email, mobile phone, work phone, website. Potential list of services for back of card: LFG Engineering and Design, GCCS Planning and Operational Consulting, Compliance Monitoring and Reporting, Routine Operations & Maintenance, Nonroutine O&M, Construction Management, Construction QA, GCCS Construction

Font styles to use
Sans Serif

Requirements
Must have
• Logo, pertinent information, maybe a tagline (still in development)
Nice to have
• For back of card, considering an engineering scale (attached for another business of ours), but want to look at other options, alternatives. Like the idea of the back of card to have some utility (scale, unit conversion info, list of services) but willing to consider lots of options.
Should not have
• Needs to have a professional (engineering) and technical look, not cartoonish.

```html
<!DOCTYPE html>
<html lang="en">
<head>
<meta charset="utf-8">
<title>Vardel GreenWorks, Inc. – Business Card</title>
<link rel="stylesheet" href="https://fonts.googleapis.com/css2?family=Montserrat:ital,wght@0,600;0,700;1,500&family=Arimo:wght@400&display=swap">
<style>
  :root {
    --page: #ffffff;
    --card-dark: #12161c;
    --card-mid: #1d2229;
    --green: #6cbd45;
    --teal: #2e9fc4;
    --grey-text: #b9bcc0;
    --white: #ffffff;
    --orange: #f39a1e;
    --red-orange: #e8492a;
  }
  * { box-sizing: border-box; margin: 0; padding: 0; }
  html, body { width: 1200px; height: 1200px; overflow: hidden; background: var(--page); }
  .sheet { position: relative; width: 1200px; height: 1200px; }

  .card {
    position: absolute; left: 121px; width: 966px; height: 553px; overflow: hidden;
  }
  .card--front { top: 39px; }
  .card--back { top: 616px; }

  .card__backdrop {
    position: absolute; inset: 0;
    background:
      radial-gradient(ellipse at 40% 30%, rgba(70,68,24,.55), transparent 55%),
      radial-gradient(ellipse at 85% 60%, rgba(60,58,22,.45), transparent 50%),
      linear-gradient(160deg, var(--card-mid), var(--card-dark) 70%);
  }

  /* Front */
  .brand {
    position: absolute; left: 192px; top: 186px;
    display: flex; align-items: center; gap: 30px;
  }
  .brand__dot {
    width: 120px; height: 120px; border-radius: 50%; background: var(--green);
  }
  .brand__name {
    font-family: "Montserrat", sans-serif; font-weight: 700;
    font-size: 66px; line-height: 1.05; color: var(--green); letter-spacing: 1px;
  }

  /* Back */
  .photo {
    position: absolute; border-radius: 100px; overflow: hidden;
    border: 4px solid var(--green);
  }
  .photo--equipment {
    left: 49px; top: 84px; width: 193px; height: 441px;
    border-color: var(--orange); border-right-color: var(--red-orange);
    background: linear-gradient(180deg, #4b79c4 0%, #7ea2d6 30%, #e0b529 55%, #b59122 70%, #b7b4ad 85%, #cfcac2 100%);
  }
  .photo--flange {
    left: 241px; top: 34px; width: 192px; height: 441px;
    background: linear-gradient(180deg, #6e7780 0%, #c4c8cc 35%, #9da3a8 60%, #e3e5e7 100%);
  }
  .photo--team {
    left: 433px; top: 84px; width: 194px; height: 441px;
    background: linear-gradient(180deg, #eeeeec 0%, #d8d4ce 30%, #c9b96a 55%, #c9a884 75%, #bdb6aa 100%);
  }

  .details { position: absolute; left: 660px; top: 86px; width: 295px; color: var(--white); }
  .details__name {
    font-family: "Montserrat", sans-serif; font-weight: 700;
    font-size: 52px; line-height: 1; color: var(--green);
  }
  .details__entity {
    font-family: "Montserrat", sans-serif; font-weight: 600;
    font-size: 29px; line-height: 1; color: var(--teal); margin-top: 10px;
  }
  .details__tagline {
    font-family: "Montserrat", sans-serif; font-style: italic; font-weight: 500;
    font-size: 15px; color: var(--grey-text); margin-top: 7px; white-space: nowrap;
  }
  .contact { position: absolute; left: 0; display: flex; align-items: center; gap: 13px;
    font-family: "Arimo", sans-serif; font-size: 21px; color: var(--white); white-space: nowrap; }
  .contact svg { width: 24px; height: 24px; flex: none; }
  .contact--phone { top: 152px; }
  .contact--email { top: 204px; }
  .contact--web { top: 268px; }
  .contact--address { top: 319px; line-height: 28px; }
  .contact--address svg { height: 32px; }
</style>
</head>
<body>
<div class="sheet">

  <section class="card card--front">
    <div class="card__backdrop" role="img" aria-label="Dark photo of industrial gas piping with yellow pipes"></div>
    <div class="brand">
      <div class="brand__dot"></div>
      <div class="brand__name">VARDEL<br>GREENWORKS</div>
    </div>
  </section>

  <section class="card card--back">
    <div class="card__backdrop" role="img" aria-label="Dark photo of industrial gas piping with yellow pipes"></div>
    <div class="photo photo--equipment" role="img" aria-label="Row of yellow pipelayer machines under blue sky"></div>
    <div class="photo photo--flange" role="img" aria-label="Close view of steel pipe flange and valve"></div>
    <div class="photo photo--team" role="img" aria-label="Engineers in hard hats reviewing plans on site"></div>

    <div class="details">
      <div class="details__name">Vardel</div>
      <div class="details__entity">GreenWorks, Inc.</div>
      <div class="details__tagline">engineering and construction firm</div>

      <div class="contact contact--phone">
        <svg viewBox="0 0 24 24"><path fill="#6cbd45" d="M6.6 2.5l3 3.6-1.8 2.4c1.2 2.8 3.4 5 6.2 6.3l2.4-1.8 3.6 3-2 3.5C10 19 4.5 13.5 3.1 4.5z"/></svg>
        <span>000-000-0000</span>
      </div>
      <div class="contact contact--email">
        <svg viewBox="0 0 24 24"><rect x="2" y="5" width="20" height="14" fill="none" stroke="#6cbd45" stroke-width="1.6"/><path d="M2 5l10 8 10-8M2 19l7.5-7M22 19l-7.5-7" fill="none" stroke="#6cbd45" stroke-width="1.6"/></svg>
        <span>info@vardel.example</span>
      </div>
      <div class="contact contact--web">
        <svg viewBox="0 0 24 24" fill="none" stroke="#6cbd45" stroke-width="1.6"><circle cx="12" cy="12" r="10"/><ellipse cx="12" cy="12" rx="4.5" ry="10"/><path d="M2 12h20M4 6.5h16M4 17.5h16"/></svg>
        <span>www.vardel.example</span>
      </div>
      <div class="contact contact--address">
        <svg viewBox="0 0 24 32"><path fill="#6cbd45" d="M12 1C6 1 1.5 5.5 1.5 11.2 1.5 18.5 12 31 12 31s10.5-12.5 10.5-19.8C22.5 5.5 18 1 12 1zm0 15a5 5 0 110-10 5 5 0 010 10z"/></svg>
        <span>Lorem Ipsum,Lorem<br>Ipsum, Lorem Ipsum<br>Ipsum, Lorem Ipsum</span>
      </div>
    </div>
  </section>

</div>
</body>
</html>
```